Business card for my new company (Accounting firm)

I need a business card for my new business Corvane Advisory and Ledger SA. Our services are accounting, tax, audit and financial management. Our customers are small companies, start-ups and new companies. The final design has to show financial security, trust and growth. Please find our logo attached to the business card. Text for the business card: Corvane Advisory and Ledger SA Tomas da Varela Director and Founder Certified Accountant Tel. 022 418 27 35 tv@corvaneconseil.ch www.corvaneconseil.ch Rue des Vergers-Bleus 14 1201 Geneva
Target Market(s)
Our customers are small companies, start-ups and new companies.
Industry/Entity Type
Finance And Accounting
Contact Information for Business Card
Corvane Conseil et Registre SA
Tomas da Varela
Directeur et Fondateur
Expert-comptable diplômé
Tél. 022 418 27 35
tv@corvaneconseil.ch
www.corvaneconseil.ch
Rue des Vergers-Bleus 14
1201 Genève

```html
<!DOCTYPE html>
<html lang="fr">
<head>
<meta charset="utf-8">
<title>Corvane Conseil et Registre SA – Carte de visite</title>
<link rel="stylesheet" href="https://fonts.googleapis.com/css2?family=Raleway:wght@400;500;700&display=swap">
<style>
  :root {
    --backdrop: #5e5e5e;
    --card-white: #f3f3f3;
    --brand-navy: #1a5b8c;
    --brand-blue: #2786c3;
    --brand-sky: #35a8dc;
    --back-blue: #185f8e;
    --text-grey: #555555;
    --text-dark: #3a3a3a;
    --white: #ffffff;
  }
  * { box-sizing: border-box; margin: 0; padding: 0; }
  html, body { width: 1200px; height: 960px; overflow: hidden; }
  body {
    background: var(--backdrop);
    font-family: "Raleway", Arial, sans-serif;
    position: relative;
  }
  .card {
    position: absolute;
    left: 270px;
    width: 660px;
    height: 377px;
    box-shadow: 0 4px 10px rgba(0,0,0,0.35);
  }
  .card--front { top: 73px; background: var(--card-white); }
  .card--back { top: 509px; background: var(--back-blue); }

  .brand-mark {
    position: absolute;
    right: 60px;
    top: 150px;
    display: flex;
    align-items: center;
    gap: 10px;
  }
  .brand-mark__square { width: 22px; height: 22px; background: var(--brand-navy); }
  .brand-mark__name {
    font-size: 34px;
    font-weight: 700;
    letter-spacing: 2px;
    color: var(--text-dark);
  }

  .person { position: absolute; left: 63px; top: 169px; }
  .person__name { font-size: 20px; font-weight: 700; color: var(--brand-navy); line-height: 26px; }
  .person__role { font-size: 15px; color: var(--text-grey); line-height: 20px; }

  .divider {
    position: absolute;
    top: 261px;
    width: 26px;
    height: 3px;
    background: var(--brand-navy);
  }
  .divider--left { left: 63px; }
  .divider--right { right: 60px; }

  .contact { position: absolute; left: 63px; top: 282px; list-style: none; }
  .contact__item {
    display: flex; align-items: center; gap: 9px;
    font-size: 15px; color: var(--text-grey); line-height: 19px;
  }
  .contact__icon { width: 12px; height: 12px; fill: none; stroke: var(--brand-navy); stroke-width: 1.4; }

  .address { position: absolute; right: 60px; top: 282px; text-align: right; font-style: normal; }
  .address__company { font-size: 15px; color: var(--brand-navy); line-height: 19px; }
  .address__line { font-size: 15px; color: var(--text-grey); line-height: 19px; }

  .colour-band { position: absolute; left: 0; bottom: 0; width: 100%; height: 10px; display: flex; }
  .colour-band span { flex: 1; }
  .colour-band__navy { background: var(--brand-navy); }
  .colour-band__blue { background: var(--brand-blue); }
  .colour-band__sky { background: var(--brand-sky); }

  .back-name {
    position: absolute; left: 0; right: 0; top: 160px;
    display: flex; justify-content: center; align-items: center; gap: 16px;
  }
  .back-name__square { width: 30px; height: 30px; background: var(--white); }
  .back-name__text { font-size: 52px; font-weight: 700; letter-spacing: 3px; color: var(--white); }
  .back-url {
    position: absolute; left: 0; right: 0; top: 317px;
    text-align: center; font-size: 15px; color: var(--white);
  }
</style>
</head>
<body>
  <section class="card card--front" aria-label="Recto de la carte">
    <div class="brand-mark">
      <span class="brand-mark__square"></span>
      <span class="brand-mark__name">CORVANE</span>
    </div>

    <div class="person">
      <h1 class="person__name">Tomas da Varela</h1>
      <p class="person__role">Directeur et Fondateur</p>
      <p class="person__role">Expert - Comptable Diplômé</p>
    </div>

    <span class="divider divider--left"></span>
    <span class="divider divider--right"></span>

    <ul class="contact">
      <li class="contact__item">
        <svg class="contact__icon" viewBox="0 0 12 12"><path d="M2 1.5 L4 1.5 L5 4 L3.8 5 Q5 7.5 7 8.2 L8 7 L10.5 8 L10.5 10 Q6 11 3 7.5 Q1 4.5 2 1.5 Z"/></svg>
        022 418 27 35
      </li>
      <li class="contact__item">
        <svg class="contact__icon" viewBox="0 0 12 12"><rect x="1" y="2.5" width="10" height="7"/><path d="M1 2.5 L6 6.5 L11 2.5"/></svg>
        tv@corvaneconseil.ch
      </li>
      <li class="contact__item">
        <svg class="contact__icon" viewBox="0 0 12 12"><circle cx="6" cy="6" r="5"/><ellipse cx="6" cy="6" rx="2.2" ry="5"/><path d="M1 6 H11"/></svg>
        www.corvaneconseil.ch
      </li>
    </ul>

    <address class="address">
      <p class="address__company">Corvane Conseil et Registre SA</p>
      <p class="address__line">Rue des Vergers-Bleus 14</p>
      <p class="address__line">1201 Genève</p>
    </address>

    <div class="colour-band">
      <span class="colour-band__navy"></span>
      <span class="colour-band__blue"></span>
      <span class="colour-band__sky"></span>
    </div>
  </section>

  <section class="card card--back" aria-label="Verso de la carte">
    <div class="back-name">
      <span class="back-name__square"></span>
      <span class="back-name__text">CORVANE</span>
    </div>
    <p class="back-url">www.corvaneconseil.ch</p>
  </section>
</body>
</html>
```